Self-Help Book Cover

This is a self-help book entitled, "Lanterns for Loners, Oddballs & Dreamers: A grounded and soulful guide to finding your footing among others."
I want the book cover to be primarily white, with red and black as secondary colors. I am open to cartoon interpretations of the words, "misfits, weirdos, and introverts" or a unique font used for each word. For the center, there can be white/gray people/balls with larger red people/balls in the middle of them shaped like an antique key. Or the center can be a red door that opens to a pleasant background image (maybe nature). This is just some ideas, I am open to others.
The author's name is Rosalind Whitcombe. The text on the back of the book is in a word doc file attached. I have also attached samples of the key and people/balls.
Updates
Requirements
Must have
- a .jpg or .tif(f) file
- at least 1000 pixels on the longest side
- ideal image height/width ratio is 1.6 (example: 1000 x 1600)
- The size should be 5.5" x 8.5"

```html
<!DOCTYPE html>
<html lang="en">
<head>
<meta charset="utf-8">
<title>Lanterns for Loners, Oddballs &amp; Dreamers — Book Cover</title>
<link rel="stylesheet" href="https://fonts.googleapis.com/css2?family=Oranienbaum&display=swap">
<style>
  :root {
    --cover-white: #f4f4f4;
    --band-red: #b51d22;
    --art-red: #c21f24;
    --art-green: #3f7a24;
    --ink: #141414;
    --stage: #d9d9d9;
  }
  html, body {
    margin: 0;
    padding: 0;
    width: 1200px;
    height: 789px;
    overflow: hidden;
    background: var(--stage);
  }
  .book-cover {
    position: absolute;
    left: 361px;
    top: 24px;
    width: 478px;
    height: 741px;
    background: var(--cover-white);
    box-shadow: 0 6px 18px rgba(0,0,0,0.25);
    font-family: "Oranienbaum", "Times New Roman", serif;
    color: var(--ink);
    overflow: hidden;
  }
  .tagline-band {
    position: absolute;
    left: 0; top: 0;
    width: 100%;
    height: 44px;
    background: var(--band-red);
    color: #fff;
    font-size: 15px;
    line-height: 44px;
    text-align: center;
    white-space: nowrap;
  }
  .title-block {
    position: absolute;
    left: 0; top: 58px;
    width: 100%;
    text-align: center;
  }
  .title-main {
    margin: 0;
    font-size: 104px;
    line-height: 1;
    font-weight: 400;
    letter-spacing: -1px;
    transform: scaleX(0.82);
  }
  .title-sub {
    margin: 2px 0 0;
    font-size: 35px;
    line-height: 1.05;
    font-weight: 400;
    transform: scaleX(0.86);
    white-space: nowrap;
  }
  .cover-art {
    position: absolute;
    left: 134px;
    top: 266px;
    width: 230px;
    height: 346px;
    background: linear-gradient(90deg, var(--art-green) 0%, var(--art-green) 48%, var(--art-red) 58%, var(--art-red) 100%);
  }
  .author {
    position: absolute;
    right: 26px;
    bottom: 74px;
    margin: 0;
    font-size: 19px;
    white-space: nowrap;
  }
  .footer-band {
    position: absolute;
    left: 0; bottom: 0;
    width: 100%;
    height: 40px;
    background: var(--band-red);
  }
</style>
</head>
<body>
  <main class="book-cover">
    <div class="tagline-band">A grounded and soulful guide to finding your footing among others.</div>

    <header class="title-block">
      <h1 class="title-main">Lanterns</h1>
      <p class="title-sub">for Loners, Oddballs &amp; Dreamers</p>
    </header>

    <div class="cover-art" role="img" aria-label="Illustration of a red door standing open onto a sunlit green forest path"></div>

    <p class="author">by Rosalind Whitcombe</p>
    <div class="footer-band"></div>
  </main>
</body>
</html>
```